IT business looking for Standout Letterhead Design

We need a letterhead design for a company based in San Diego, CA called Corvane Systems, Inc. We specialize in IT engineering, installation and technical support pertaining to the department of defense.

We would like to see a design that incorporates the black and gold that matches our company logo.

More information on the company can be found at www.corvane-sys.example

```html
<!DOCTYPE html>
<html lang="en">
<head>
<meta charset="utf-8">
<title>Corvane Systems, Inc. — Letterhead</title>
<link href="https://fonts.googleapis.com/css2?family=Questrial&display=swap" rel="stylesheet">
<style>
  :root {
    --ink: #000000;
    --paper: #ffffff;
    --gold-bright: #fff200;
    --gold-mid: #e3b70a;
    --bronze: #9a5a12;
    --bronze-dark: #3a1f05;
    --text: #1a1a1a;
  }
  html, body {
    margin: 0;
    padding: 0;
    overflow: hidden;
    background: var(--paper);
  }
  .letterhead {
    position: relative;
    width: 963px;
    height: 1200px;
    background: var(--paper);
    overflow: hidden;
    font-family: "Questrial", "Century Gothic", sans-serif;
    color: var(--text);
  }
  .header-art {
    position: absolute;
    left: 0;
    top: 0;
    width: 963px;
    height: 180px;
  }
  .brand {
    position: absolute;
    left: 0;
    width: 963px;
    top: 140px;
    text-align: center;
  }
  .brand-name {
    font-family: "Questrial", "Century Gothic", sans-serif;
    font-size: 21px;
    letter-spacing: 1px;
    color: var(--ink);
    margin: 0;
    font-weight: 400;
  }
  .footer-rule {
    position: absolute;
    left: 0;
    top: 1129px;
    width: 963px;
    height: 8px;
  }
  .contact {
    position: absolute;
    display: flex;
    align-items: center;
    gap: 7px;
    font-size: 16px;
    line-height: 1;
    white-space: nowrap;
  }
  .contact svg { flex: none; }
  .contact .skype-dot {
    width: 13px;
    height: 13px;
    border-radius: 50%;
    background: var(--ink);
    margin-left: -3px;
    margin-right: 0;
  }
  .c-company { left: 116px; top: 1157px; }
  .c-city    { left: 119px; top: 1184px; }
  .c-phone   { left: 412px; top: 1157px; }
  .c-fax     { left: 412px; top: 1184px; }
  .c-email   { left: 654px; top: 1157px; }
  .c-web     { left: 654px; top: 1184px; }
</style>
</head>
<body>
<main class="letterhead">

  <svg class="header-art" viewBox="0 0 963 180" aria-hidden="true">
    <defs>
      <linearGradient id="band-rule" x1="0" x2="1" y1="0" y2="0">
        <stop offset="0" stop-color="var(--bronze-dark)"/>
        <stop offset="0.2" stop-color="var(--bronze)"/>
        <stop offset="0.35" stop-color="var(--gold-mid)"/>
        <stop offset="0.5" stop-color="var(--gold-bright)"/>
        <stop offset="0.65" stop-color="var(--gold-mid)"/>
        <stop offset="0.82" stop-color="var(--bronze)"/>
        <stop offset="1" stop-color="var(--ink)"/>
      </linearGradient>
      <linearGradient id="arch-rim" x1="0" x2="0" y1="0" y2="1">
        <stop offset="0" stop-color="var(--gold-bright)"/>
        <stop offset="1" stop-color="var(--gold-mid)"/>
      </linearGradient>
    </defs>
    <rect class="header-band" x="0" y="0" width="963" height="162" fill="var(--ink)"/>
    <rect class="header-rule" x="0" y="153" width="963" height="9" fill="url(#band-rule)"/>
    <path class="header-arch" d="M334 162 A146 116 0 0 1 626 162 Z"
          fill="var(--paper)" stroke="url(#arch-rim)" stroke-width="10"/>
    <rect x="320" y="162" width="320" height="18" fill="var(--paper)"/>
    <circle class="brand-mark" cx="480" cy="100" r="24" fill="var(--gold-mid)"/>
  </svg>

  <div class="brand">
    <p class="brand-name">Corvane Systems, Inc.</p>
  </div>

  <svg class="footer-rule" viewBox="0 0 963 8" aria-hidden="true">
    <defs>
      <linearGradient id="foot-rule" x1="0" x2="1" y1="0" y2="0">
        <stop offset="0" stop-color="var(--bronze-dark)"/>
        <stop offset="0.25" stop-color="var(--bronze)"/>
        <stop offset="0.5" stop-color="var(--gold-bright)"/>
        <stop offset="0.75" stop-color="var(--bronze)"/>
        <stop offset="1" stop-color="var(--ink)"/>
      </linearGradient>
    </defs>
    <rect x="65" y="2" width="833" height="4" fill="url(#foot-rule)"/>
  </svg>

  <div class="contact c-company">
    <svg width="16" height="17" viewBox="0 0 16 17" aria-hidden="true">
      <rect x="1" y="1" width="10" height="15" fill="none" stroke="#000" stroke-width="1.4"/>
      <rect x="11" y="7" width="4" height="9" fill="none" stroke="#000" stroke-width="1.4"/>
      <g fill="#000"><rect x="3" y="3" width="2" height="2"/><rect x="7" y="3" width="2" height="2"/><rect x="3" y="7" width="2" height="2"/><rect x="7" y="7" width="2" height="2"/><rect x="3" y="11" width="2" height="2"/><rect x="7" y="11" width="2" height="2"/></g>
    </svg>
    <span>Corvane Systems, Inc.</span>
  </div>
  <div class="contact c-city">
    <svg width="10" height="14" viewBox="0 0 10 14" aria-hidden="true">
      <path d="M5 0a5 5 0 0 1 5 5c0 3.5-5 9-5 9S0 8.5 0 5a5 5 0 0 1 5-5z" fill="#000"/>
      <circle cx="5" cy="5" r="1.8" fill="#fff"/>
    </svg>
    <span>San Diego, CA</span>
  </div>

  <div class="contact c-phone">
    <svg width="15" height="15" viewBox="0 0 15 15" aria-hidden="true">
      <path d="M3 0.5l2.5 3-1.3 1.8c.8 2 2.4 3.7 4.5 4.6l1.8-1.3 3 2.5-1.6 2.9C6.5 13.5 1.5 8.5 0.5 2.1z" fill="#000"/>
    </svg>
    <span class="skype-dot" aria-hidden="true"></span>
    <span>619-555-0142</span>
  </div>
  <div class="contact c-fax">
    <svg width="15" height="14" viewBox="0 0 15 14" aria-hidden="true">
      <rect x="3" y="0" width="9" height="4" fill="#000"/>
      <rect x="0" y="4.5" width="15" height="6.5" rx="1" fill="#000"/>
      <rect x="3" y="8.5" width="9" height="5.5" fill="#000" stroke="#fff" stroke-width="1"/>
    </svg>
    <span class="skype-dot" aria-hidden="true"></span>
    <span>619-555-0187</span>
  </div>

  <div class="contact c-email">
    <svg width="14" height="10" viewBox="0 0 14 10" aria-hidden="true">
      <rect x="0" y="0" width="14" height="10" fill="#000"/>
      <path d="M0 0l7 5.5L14 0" fill="none" stroke="#fff" stroke-width="1.2"/>
    </svg>
    <span>info@corvane-sys.example</span>
  </div>
  <div class="contact c-web">
    <svg width="15" height="15" viewBox="0 0 15 15" aria-hidden="true">
      <g fill="none" stroke="#000" stroke-width="1.3">
        <circle cx="7.5" cy="7.5" r="6.6"/>
        <ellipse cx="7.5" cy="7.5" rx="3" ry="6.6"/>
        <path d="M1 7.5h13M2 4h11M2 11h11"/>
      </g>
    </svg>
    <span>www.corvane-sys.example</span>
  </div>

</main>
</body>
</html>
```